Business Card for Business consulting practice

Need a design for a consultant business card. Simple and elegant.
I need the following information on the card:
Logo: (see uploaded file)
Company name: Calmora Advisory Group
Name: Dana Weltrup
Title: Managing Director - Aerospace and Defence
Phone #: 514-268-3917
e-mail: dana.weltrup@calmora-example.com
Website: www.calmora-example.com
Tagline: Proposals Management and Capture support for complex procurements

```html
<!DOCTYPE html>
<html lang="en">
<head>
<meta charset="utf-8">
<title>Calmora Advisory Group – Business Card</title>
<link rel="stylesheet" href="https://fonts.googleapis.com/css2?family=Cinzel:wght@700&family=Arimo:wght@400&display=swap">
<style>
  :root{
    --backdrop:#1c1d20;
    --navy:#0d2c40;
    --navy-deep:#0a2334;
    --accent:#2a96c8;
    --paper:#ffffff;
    --ink:#0d2c40;
    --text-light:#ffffff;
  }
  *{margin:0;padding:0;box-sizing:border-box}
  html,body{width:1200px;height:948px;overflow:hidden;background:var(--backdrop)}
  .canvas{width:1200px;height:948px;display:flex;flex-direction:column;align-items:center;justify-content:center;gap:54px}
  .card{position:relative;width:700px;height:400px;border-radius:26px;background:var(--navy);overflow:hidden;color:var(--text-light);font-family:"Arimo",Arial,sans-serif}

  /* front */
  .front-halo{position:absolute;right:-70px;top:-120px;width:440px;height:440px;border-radius:50%;
    background:radial-gradient(circle at 60% 30%,#16415c 0%,var(--navy-deep) 70%)}
  .front-brand{position:absolute;left:60px;top:230px;width:600px}
  .wordmark{font-family:"Cinzel",Georgia,serif;font-weight:700;letter-spacing:.5px;line-height:1.1;white-space:nowrap}
  .front-brand .wordmark{color:var(--text-light);font-size:30px}
  .brand-rule{height:2px;background:var(--accent);margin:12px 0 16px;width:440px}
  .tagline{font-size:19px;line-height:1.3;color:var(--text-light)}

  /* back */
  .back-disc{position:absolute;left:420px;top:-150px;width:440px;height:440px;border-radius:50%;
    background:var(--paper);box-shadow:-4px 6px 0 0 var(--accent)}
  .back-brand{position:absolute;left:465px;top:110px;width:230px}
  .back-brand .wordmark{color:var(--ink);font-size:28px;line-height:1.2;white-space:normal}
  .identity{position:absolute;left:0;top:120px;padding-left:58px}
  .identity::before{content:"";position:absolute;left:0;top:8px;width:24px;height:86px;background:var(--accent)}
  .person-name{font-family:"Cinzel",Georgia,serif;font-weight:700;font-size:30px;color:var(--accent);letter-spacing:.5px}
  .person-title{font-size:19px;line-height:1.25;margin-top:4px}
  .contact{position:absolute;left:58px;top:260px;font-size:18px;line-height:1.35}
  .contact-line{display:flex;align-items:center;gap:10px}
  .contact-line svg{width:16px;height:16px;flex:none}
  .address{margin-bottom:6px}
</style>
</head>
<body>
<main class="canvas">

  <section class="card card-front">
    <div class="front-halo"></div>
    <div class="front-brand">
      <div class="wordmark">Calmora Advisory Group</div>
      <div class="brand-rule"></div>
      <p class="tagline">Proposals Management and Capture<br>support for complex procurements</p>
    </div>
  </section>

  <section class="card card-back">
    <div class="back-disc"></div>
    <div class="back-brand">
      <div class="wordmark">Calmora Advisory Group</div>
    </div>

    <div class="identity">
      <h1 class="person-name">DANA WELTRUP</h1>
      <p class="person-title">Managing Director -<br>Aerospace and Defence</p>
    </div>

    <div class="contact">
      <p class="address">880 Linden Crescent<br>Ste 210, Marlow Vale, ON 4190</p>
      <p class="contact-line">
        <svg viewBox="0 0 16 16" aria-hidden="true"><path d="M3 2l3 0 1 3-2 1.5c.8 1.7 2 2.9 3.5 3.5L10 8l3 1v3c0 .6-.4 1-1 1C6.5 13 3 9.5 3 4c0-.6.4-1 1-1z" fill="var(--accent)"/></svg>
        514-268-3917</p>
      <p class="contact-line">
        <svg viewBox="0 0 16 16" aria-hidden="true"><rect x="1" y="3" width="14" height="10" rx="1" fill="var(--accent)"/><path d="M1.5 4 8 9l6.5-5" stroke="var(--navy)" stroke-width="1.4" fill="none"/></svg>
        dana.weltrup@calmora-example.com</p>
      <p class="contact-line">
        <svg viewBox="0 0 16 16" aria-hidden="true"><circle cx="8" cy="8" r="6.5" fill="none" stroke="var(--accent)" stroke-width="1.5"/><path d="M1.5 8h13M8 1.5c2.2 2.4 2.2 10.6 0 13M8 1.5c-2.2 2.4-2.2 10.6 0 13" stroke="var(--accent)" stroke-width="1.2" fill="none"/></svg>
        www.calmora-example.com</p>
    </div>
  </section>

</main>
</body>
</html>
```